依頼詳細
現在木曜日のみ休診となっていますが、獣医が一人増えることにより2020年2月1日より全曜日で診察を行うことを予定しています(盆、年末年始、GW除く)。
その告知をするためのチラシをポスティング、新聞折り込みで配布する予定で、その告知チラシのデザインをお願いしたいです。表面は動物病院の告知で、裏面は併設のトリミングサロンの宣伝をしたいと思っています。思わず引きつかれるようなデザインをお願いしたいです。
(表面)
・添付のミドリツバメ便の画像のイメージで「木曜日休診」が「全曜日診察」(盆、年末年始、GWは除く)へ変わることを告知したいです
・キャラクターは犬と猫のイラストでお願いしたいです
・全体的なデザインはシンプルで遊び心があるものにしてほしいです
・看板(暖簾)の写真(添付)も載せてほしいです(これは小さくてよいです)
(裏面)
・犬が猫足バスタブに浸かって、楽しそうにしているイメージでお願いします
・こちらもシンプルで遊び心のあるデザインでお願いしたいです
・トリミングは「シャンプーのみ」、「シャンプー&カット」のコースがあり、両コースに爪切り、足裏バリカン、耳掃除、お腹バリカン、肛門バリカン、肛門嚢絞りを含むことを記載してほしいです
・動物病院併設なのでシニア犬、持病持ちの犬も対応可能と載せてほしいです
・看板(暖簾)の写真(添付)も載せてほしいです(これも小さくてよいです)
記載項目
【表面】
動物病院ひだまり 若草台
京都市西京区小川原南町17 メゾン葵野2階
電話番号 0756147328
診察時間 午前9:30~12:30 予約診察16:00~16:45 午後17:00~20:00
(日、祝日は午前のみ)
全曜日診察(盆、正月、GWは除く)
獣医師名 院長 青柳航平 副院長 村瀬譲
駐車場5台完備(トリミングサロン共用)
駐車場地図(添付)
【裏面】
トリミングサロン凛(動物病院ひだまり 若草台 併設)
電話番号 0756281945
営業時間 9:00~18:00
店休日 木曜日 日曜日
店長名 北條葉月
駐車場5台完備(動物病院共用)
ペットホテル完備
トリミング料金 (税抜き)
・トイプードル シャンプー3780円~ シャンプー&カット6480円~
・チワワ シャンプー2980円~ シャンプー&カット4480円~
・ヨークシャーテリア シャンプー3280円~ シャンプー&カット5780円~
その他全犬種対応可能
ペットホテル料金(1泊2日、税抜き)
・小型犬 2980円 ・中型犬 3980円 ・大型犬 4980円
一時預かりも可能
サイズ
A3
ページ数
両面
希望イメージ
シンプル 複雑
単色 カラフル
暗い 明るい
日常 高級
遊び心 厳粛
未来的 伝統的
女性的 男性的
希望する色
黄・オレンジ系、緑系、茶系
納品ファイル
補足説明
手直しのやり取りは基本的に少なく(5回以下に)したいと思いますが、納得のいくものを制作していただきたいので、出来れば制限を設けないようにしてもらいたいです

診察表を使った表現が、病院であることが分かりやすく気に入りました。

この度はコンペに応募していただきありがとうございました。

```html
<!DOCTYPE html>
<html lang="ja">
<head>
<meta charset="utf-8">
<title>トリミングサロン凛</title>
<link href="https://fonts.googleapis.com/css2?family=Noto+Sans+JP:wght@400;500;700&family=Noto+Serif+JP:wght@400;600;700;900&display=swap" rel="stylesheet">
<style>
:root{
  --cream:#f4efe7;
  --paper:#fbf8f3;
  --brown:#8a6a4c;
  --brown-dark:#5e4632;
  --brown-light:#c8b49b;
  --line:#d8cbb8;
  --green:#8fa52a;
  --red:#d8483a;
  --ink:#4a3c30;
  --white:#ffffff;
  --badge:#3f4247;
}
*{margin:0;padding:0;box-sizing:border-box}
html,body{width:846px;height:1200px;overflow:hidden;background:var(--cream)}
body{font-family:"Noto Sans JP",sans-serif;color:var(--ink)}
.flyer{position:relative;width:846px;height:1200px;overflow:hidden;background:var(--paper)}

.hero-photo{position:absolute;left:0;top:0;width:846px;height:650px;
  background:radial-gradient(ellipse 60% 40% at 55% 72%,#ffffff 0%,#f1ece4 60%,rgba(241,236,228,0) 100%),
  linear-gradient(180deg,#ede7de 0%,#f4efe8 55%,#e9e2d7 100%)}

.brand{position:absolute;left:46px;top:34px;font-family:"Noto Serif JP",serif;color:var(--brown-dark)}
.brand-parent{font-size:19px;font-weight:600;letter-spacing:.08em}
.brand-name{font-size:46px;font-weight:700;letter-spacing:.08em;margin-top:8px;line-height:1.2}

.partner{position:absolute;right:40px;top:74px;display:flex;align-items:center;gap:10px;
  font-family:"Noto Serif JP",serif;font-weight:600;font-size:17px;color:var(--brown-dark)}
.partner i{display:block;width:22px;height:22px;background:var(--badge)}

.reassure{position:absolute;right:36px;top:226px;width:200px;height:150px;background:var(--green);
  border-radius:16px;color:var(--white);font-weight:700;font-size:29px;line-height:1.35;
  display:flex;align-items:center;justify-content:center;text-align:center}

.features{position:absolute;left:250px;top:370px;list-style:none}
.features li{display:flex;align-items:center;gap:12px;font-size:22px;font-weight:700;color:var(--ink);margin-bottom:12px}
.features small{font-size:14px;font-weight:500}
.features svg{width:30px;height:30px;flex:none}

.section-title{position:absolute;left:0;width:846px;display:flex;align-items:center;justify-content:center;gap:18px}
.section-title::before,.section-title::after{content:"";height:1px;width:220px;background:var(--brown-light)}
.section-title span{background:var(--brown);color:var(--white);font-family:"Noto Serif JP",serif;font-size:19px;
  letter-spacing:.15em;padding:5px 34px;border-radius:3px}

.price-table{position:absolute;left:66px;width:714px;border-collapse:collapse;font-size:17px}
.price-table th{background:#efe6d9;color:var(--brown);font-weight:500;font-size:15px;text-align:left;padding:8px 14px}
.price-table td{padding:10px 14px;border-bottom:1px solid var(--line)}
.price-table td:first-child{width:36%}
.note{position:absolute;font-size:12px;color:var(--brown)}
.course-note{position:absolute;left:66px;top:920px;font-size:14.5px;color:var(--ink)}

.hotel{position:absolute;left:66px;top:1015px;width:714px}
.hotel-cond{background:#efe6d9;padding:7px 14px;font-size:15px;color:var(--brown)}
.hotel-cond small{font-size:12px;margin-left:10px}
.hotel-rates{display:flex;justify-content:space-between;padding:10px 14px;font-size:17px;border-bottom:1px solid var(--line)}

.contact{position:absolute;left:0;bottom:0;width:846px;height:84px;background:var(--green);color:var(--white);
  display:flex;align-items:center;justify-content:space-between;padding:0 34px}
.contact-lead{display:flex;align-items:center;gap:14px}
.contact-lead svg{width:46px;height:46px}
.contact-lead strong{display:block;font-size:25px;font-weight:700;line-height:1.3}
.contact-lead span{font-size:14px}
.contact-tel{text-align:right}
.contact-tel strong{display:block;font-size:38px;font-weight:700;letter-spacing:.02em;line-height:1.1}
.contact-tel span{font-size:13px}
</style>
</head>
<body>
<div class="flyer">
  <div class="hero-photo" role="img" aria-label="猫足バスタブに浸かる茶色の子犬の写真"></div>

  <header class="brand">
    <p class="brand-parent">動物病院ひだまり 若草台　併設</p>
    <h1 class="brand-name">トリミングサロン凛</h1>
  </header>

  <div class="partner"><i></i>動物病院ひだまり 若草台</div>

  <div class="reassure">動物病院<br>併設で<br>安心！</div>

  <ul class="features">
    <li><svg viewBox="0 0 30 30" aria-hidden="true"><rect x="2" y="6" width="22" height="22" fill="#fff" stroke="#d8483a" stroke-width="2.5"/><path d="M7 15l6 7L28 3" fill="none" stroke="#d8483a" stroke-width="4"/></svg>全犬種対応可能</li>
    <li><svg viewBox="0 0 30 30" aria-hidden="true"><rect x="2" y="6" width="22" height="22" fill="#fff" stroke="#d8483a" stroke-width="2.5"/><path d="M7 15l6 7L28 3" fill="none" stroke="#d8483a" stroke-width="4"/></svg>シニア犬、持病持ちの犬も対応可能</li>
    <li><svg viewBox="0 0 30 30" aria-hidden="true"><rect x="2" y="6" width="22" height="22" fill="#fff" stroke="#d8483a" stroke-width="2.5"/><path d="M7 15l6 7L28 3" fill="none" stroke="#d8483a" stroke-width="4"/></svg>ペットホテル完備</li>
    <li><svg viewBox="0 0 30 30" aria-hidden="true"><rect x="2" y="6" width="22" height="22" fill="#fff" stroke="#d8483a" stroke-width="2.5"/><path d="M7 15l6 7L28 3" fill="none" stroke="#d8483a" stroke-width="4"/></svg>駐車場5台完備<small>（動物病院共用）</small></li>
  </ul>

  <h2 class="section-title" style="top:682px"><span>トリミング料金</span></h2>
  <table class="price-table" style="top:730px">
    <tr><th>犬種例（全犬種対応可能）</th><th>シャンプー</th><th>シャンプー＆カット</th></tr>
    <tr><td>トイプードル</td><td>3780円～</td><td>6480円～</td></tr>
    <tr><td>チワワ</td><td>2980円～</td><td>4480円～</td></tr>
    <tr><td>ヨークシャーテリア</td><td>3280円～</td><td>5780円～</td></tr>
  </table>
  <p class="note" style="right:66px;top:900px">※税抜き価格</p>
  <p class="course-note">両コースに爪切り、足裏バリカン、耳掃除、お腹バリカン、肛門バリカン、肛門嚢絞りを含みます。</p>

  <h2 class="section-title" style="top:966px"><span>ペットホテル料金</span></h2>
  <div class="hotel">
    <p class="hotel-cond">1泊2日ご利用時<small>※一時預かりも可能</small></p>
    <p class="hotel-rates"><span>小型犬　2980円</span><span>中型犬　3980円</span><span>大型犬　4980円</span></p>
  </div>
  <p class="note" style="right:66px;top:1096px">※税抜き価格</p>

  <footer class="contact">
    <div class="contact-lead">
      <svg viewBox="0 0 50 50" aria-hidden="true"><circle cx="25" cy="25" r="24" fill="none" stroke="#fff" stroke-width="2"/><path d="M17 12c2-1 4 0 5 2l2 5c1 2 0 3-1 4l-2 1c1 4 4 7 8 8l1-2c1-1 2-2 4-1l5 2c2 1 3 3 2 5l-1 2c-2 2-5 3-9 1-7-3-13-9-16-16-2-4-1-7 1-9z" fill="#fff"/></svg>
      <div><strong>ご予約の際はお電話ください</strong><span>店長名　北條葉月</span></div>
    </div>
    <div class="contact-tel">
      <strong>075-628-1945</strong>
      <span>営業時間 9:00～18:00　店休日 木曜日、日曜日</span>
    </div>
  </footer>
</div>
</body>
</html>
```